security services Business Card Design

i would like a business card for our security company. i would like the colours to match the logo. or other bright colours can be used. would like it too look professional and smart.

Industry/Entity Type

Security

Contact Information for Business Card

Harbor Crest Security management Tomas Brevik Managing Directorph: 1300 747 433m: 0413 065 438e: nader@harborcrestsecurity.com.auw: www.harborcrestsecuritygroup.com.au

Font styles to use
Serif

Colors
85cae6
0393ce
0655a3
3276b5
fdfdfd
000000
886aae
f04a51
6b449b

Requirements
Must have
• Facebook logo at the back.
• also at the back with bullet points of
• -Concierge
• -public Events
• -Private events
• -Corporate
• -static Guards
• -residential

```html
<!DOCTYPE html>
<html lang="en">
<head>
<meta charset="utf-8">
<title>Harbor Crest Security management – Business Card</title>
<link rel="stylesheet" href="https://fonts.googleapis.com/css2?family=Tinos:wght@400;700&display=swap">
<style>
  :root {
    --backdrop-light: #e3e5e2;
    --backdrop-dark: #c9ccc8;
    --card: #fdfdfd;
    --ink: #000000;
    --brand-blue: #3276b5;
    --bullet-blue: #0655a3;
    --muted: #555555;
  }
  * { margin: 0; padding: 0; box-sizing: border-box; }
  html, body { width: 1200px; height: 1000px; overflow: hidden; }
  body {
    background: radial-gradient(ellipse at 50% 40%, var(--backdrop-light), var(--backdrop-dark));
    font-family: "Tinos", "Times New Roman", serif;
    color: var(--ink);
    position: relative;
  }
  .card {
    position: absolute;
    width: 580px;
    height: 320px;
    background: var(--card);
    border-radius: 34px;
    box-shadow: 0 10px 24px rgba(0,0,0,0.18);
    display: flex;
    align-items: center;
  }
  .card--back { left: 530px; top: 150px; }
  .card--front { left: 110px; top: 540px; }

  .brand {
    width: 250px;
    padding-left: 50px;
    display: flex;
    align-items: center;
    gap: 12px;
  }
  .brand__dot {
    flex: none;
    width: 18px; height: 18px;
    border-radius: 50%;
    background: var(--brand-blue);
  }
  .brand__name {
    font-weight: 700;
    font-size: 24px;
    line-height: 1.15;
    color: var(--brand-blue);
  }

  .services { list-style: none; padding-left: 20px; }
  .services__item {
    font-weight: 700;
    font-size: 17px;
    letter-spacing: 3px;
    line-height: 1.45;
    display: flex;
    align-items: center;
  }
  .services__item::before {
    content: "";
    width: 6px; height: 6px;
    border-radius: 50%;
    background: var(--bullet-blue);
    margin-right: 14px;
  }
  .social {
    margin-top: 6px;
    display: flex;
    align-items: center;
    gap: 8px;
    font-size: 14px;
    color: var(--muted);
  }
  .social__square {
    width: 12px; height: 12px;
    background: var(--bullet-blue);
    border-radius: 2px;
  }

  .contact { padding-left: 10px; }
  .contact__name {
    font-weight: 700;
    font-size: 27px;
    letter-spacing: 1px;
    color: var(--brand-blue);
  }
  .contact__title {
    font-weight: 700;
    font-size: 14px;
    letter-spacing: 1px;
    margin-bottom: 6px;
  }
  .contact__row {
    display: flex;
    align-items: center;
    gap: 10px;
    font-weight: 700;
    font-size: 18px;
    letter-spacing: 2px;
    line-height: 1.3;
  }
  .contact__row svg { width: 14px; height: 14px; flex: none; }
  .contact__line { font-size: 14px; line-height: 1.4; }
</style>
</head>
<body>

  <section class="card card--back" aria-label="Business card back">
    <div class="brand">
      <span class="brand__dot"></span>
      <span class="brand__name">Harbor Crest Security management</span>
    </div>
    <div class="services-block">
      <ul class="services">
        <li class="services__item">Concierge</li>
        <li class="services__item">Public Events</li>
        <li class="services__item">Private Events</li>
        <li class="services__item">Corporate</li>
        <li class="services__item">Static Guards</li>
        <li class="services__item">Residential</li>
      </ul>
      <div class="social"><span class="social__square"></span>harborcrestsecurity</div>
    </div>
  </section>

  <section class="card card--front" aria-label="Business card front">
    <div class="brand">
      <span class="brand__dot"></span>
      <span class="brand__name">Harbor Crest Security management</span>
    </div>
    <div class="contact">
      <div class="contact__name">Tomas Brevik</div>
      <div class="contact__title">MANAGING DIRECTORPH</div>
      <div class="contact__row">
        <svg viewBox="0 0 24 24" aria-hidden="true"><path fill="#0655a3" d="M6.6 10.8a15.1 15.1 0 0 0 6.6 6.6l2.2-2.2a1 1 0 0 1 1-.25 11.4 11.4 0 0 0 3.6.57 1 1 0 0 1 1 1V20a1 1 0 0 1-1 1A17 17 0 0 1 3 4a1 1 0 0 1 1-1h3.5a1 1 0 0 1 1 1c0 1.25.2 2.45.57 3.57a1 1 0 0 1-.25 1z"/></svg>
        1300 582 916
      </div>
      <div class="contact__row">
        <svg viewBox="0 0 24 24" aria-hidden="true"><rect x="6" y="2" width="12" height="20" rx="2" fill="none" stroke="#0655a3" stroke-width="2.4"/><circle cx="12" cy="18" r="1.3" fill="#0655a3"/></svg>
        0427 391 804
      </div>
      <div class="contact__line">tomas@harborcrestsecuritygroup.com.au</div>
      <div class="contact__line">www.harborcrestsecuritygroup.com.au</div>
    </div>
  </section>

</body>
</html>
```